Physical Large Banner For Corporate Event

Hi, we would like a large banner designed for a corporate event using adobe illustrator/pdf. The size of the banner must be 2000 (h)x800 (w) mm to fit with the printing requirements (please visit https://www.inkvaleprints.com/products/48/banner-stands and see the guidelines for size for a standard banner)

Our organisation holds events for students to find out more on top careers such as Investment Banking & Law. The banner design can be fairly simple but bold using the same themes and colours on our website www.brightlanefutures.co.uk. We can provide imagery of our logo for use/other pictures requested such as those for students/cityscapes etc.

The only text on the banner should be our web address at the bottom (www.brightlanefutures.co.uk) and a line that says "A Head Start in the City, We bring the internship to you..." like in our website homepage.

Target Market(s)

Students & Graduate Recruiters

Industry/Entity Type

Education

Requirements
Must have
• Website address
• Cool imagery
Should not have
• Too much clutter, clean and simple pleaseE

```html
<!DOCTYPE html>
<html lang="en">
<head>
<meta charset="utf-8">
<title>Brightlane – Event Banner Set</title>
<link rel="stylesheet" href="https://fonts.googleapis.com/css2?family=Open+Sans:wght@400;600&display=swap">
<style>
  :root {
    --backdrop: #ecebe8;
    --banner-white: #ffffff;
    --brand-red: #7a1a24;
    --brand-grey: #5f5f62;
    --text-grey: #58595b;
    --sky: #f4f6f9;
    --tower-blue: #56637c;
    --tower-steel: #8d9bb0;
  }
  * { box-sizing: border-box; margin: 0; padding: 0; }
  html, body {
    width: 1200px; height: 1119px; overflow: hidden;
    background: var(--backdrop);
    font-family: "Open Sans", Arial, sans-serif;
  }
  .banner-set {
    position: relative; width: 1200px; height: 1119px;
  }
  .banner {
    position: absolute; top: 134px;
    width: 340px; height: 850px;
    background: var(--banner-white);
    box-shadow: 0 2px 10px rgba(0,0,0,0.12);
  }
  .banner--left { left: 40px; }
  .banner--centre { left: 430px; }
  .banner--right { left: 820px; }

  .web-address {
    position: absolute; left: 0; right: 0;
    display: flex; align-items: center; justify-content: center; gap: 7px;
    color: var(--brand-red); font-size: 21px; font-weight: 400;
  }
  .web-address svg { width: 17px; height: 17px; flex: none; }

  .brand-name {
    position: absolute; left: 0; right: 0; text-align: center;
    color: var(--brand-grey); font-size: 50px; font-weight: 400;
    letter-spacing: 0.5px; line-height: 1;
  }

  .tagline {
    position: absolute; left: 0; right: 0; text-align: center;
    color: var(--text-grey);
  }
  .tagline__lead { display: block; font-size: 22px; line-height: 1.2; }
  .tagline__sub { display: block; font-size: 16px; line-height: 1.3; margin-top: 2px; }

  .cityscape {
    position: absolute; left: 8px; right: 8px;
    background:
      linear-gradient(180deg, rgba(255,255,255,0.55) 0%, rgba(255,255,255,0) 55%),
      linear-gradient(90deg, var(--tower-blue) 0%, var(--tower-steel) 16%, var(--sky) 34%, #ffffff 50%, var(--sky) 66%, var(--tower-steel) 84%, var(--tower-blue) 100%);
  }

  /* left & right layout */
  .banner--left .web-address, .banner--right .web-address { top: 78px; }
  .banner--left .brand-name, .banner--right .brand-name { top: 245px; }
  .banner--left .tagline, .banner--right .tagline { top: 355px; }
  .banner--left .cityscape, .banner--right .cityscape { top: 420px; bottom: 48px; }

  /* centre layout */
  .banner--centre .brand-name { top: 180px; }
  .banner--centre .tagline { top: 285px; }
  .banner--centre .web-address { top: 368px; }
  .banner--centre .cityscape { top: 420px; bottom: 60px; }
</style>
</head>
<body>
<main class="banner-set">

  <section class="banner banner--left">
    <p class="web-address">
      <svg viewBox="0 0 20 20" aria-hidden="true"><g fill="none" stroke="currentColor" stroke-width="1.6"><circle cx="10" cy="10" r="8.2"/><ellipse cx="10" cy="10" rx="3.6" ry="8.2"/><path d="M2 10h16M3.4 5.6h13.2M3.4 14.4h13.2"/></g></svg>
      brightlanefutures.co.uk
    </p>
    <h2 class="brand-name">Brightlane</h2>
    <p class="tagline">
      <span class="tagline__lead">A Head Start in the City</span>
      <span class="tagline__sub">We bring the internship to you...</span>
    </p>
    <div class="cityscape" role="img" aria-label="Upward view of glass skyscrapers against a bright sky"></div>
  </section>

  <section class="banner banner--centre">
    <h2 class="brand-name">Brightlane</h2>
    <p class="tagline">
      <span class="tagline__lead">A Head Start in the City</span>
      <span class="tagline__sub">We bring the internship to you...</span>
    </p>
    <p class="web-address">
      <svg viewBox="0 0 20 20" aria-hidden="true"><g fill="none" stroke="currentColor" stroke-width="1.6"><circle cx="10" cy="10" r="8.2"/><ellipse cx="10" cy="10" rx="3.6" ry="8.2"/><path d="M2 10h16M3.4 5.6h13.2M3.4 14.4h13.2"/></g></svg>
      brightlanefutures.co.uk
    </p>
    <div class="cityscape" role="img" aria-label="Upward view of glass skyscrapers against a bright sky"></div>
  </section>

  <section class="banner banner--right">
    <p class="web-address">
      <svg viewBox="0 0 20 20" aria-hidden="true"><g fill="none" stroke="currentColor" stroke-width="1.6"><circle cx="10" cy="10" r="8.2"/><ellipse cx="10" cy="10" rx="3.6" ry="8.2"/><path d="M2 10h16M3.4 5.6h13.2M3.4 14.4h13.2"/></g></svg>
      brightlanefutures.co.uk
    </p>
    <h2 class="brand-name">Brightlane</h2>
    <p class="tagline">
      <span class="tagline__lead">A Head Start in the City</span>
      <span class="tagline__sub">We bring the internship to you...</span>
    </p>
    <div class="cityscape" role="img" aria-label="Upward view of glass skyscrapers against a bright sky"></div>
  </section>

</main>
</body>
</html>
```